Driving-coach/trainer who wants to inform about the offer and how I can help people to drive more re

I need a flyer that informs potential customers about my offer.

DL size 210 mm x 99 mm, vertical!

I'm a trainer/coach who helps people to drive a car more relaxed, without fear and more confident.

It's a one to one training. I do train people in their own car. It gets people their freedom back to go where and when they like to go by own car...

Target Market(s)

People (man an woman) who are afraid of driving a car, or are very stressed while driving....

Industry/Entity Type

Life Coaching

Font styles to use
Sans Serif

Colors
acd136

Requirements
Must have
• Page 1:
• -my offer (see text-pdf)
• -three fotos (see attached files "Pixmarra") of people who are satisfied with my offer
• Page 2:
• -advantages in the work with me.
• -contact information
• -and a picture of me (see attached file) next to the contact information or the advantages of my work
• -my logo (see attached file) on Page 1 + 2
• -i like a "clear" and structured layout. "Less is more"

```html
<!DOCTYPE html>
<html lang="de">
<head>
<meta charset="utf-8">
<title>Fahrsicher-Coaching – Flyer</title>
<link rel="stylesheet" href="https://fonts.googleapis.com/css2?family=Advent+Pro:wght@400;500&family=Raleway:wght@300&display=swap">
<style>
:root{
  --panel:#a29a98;
  --gap:#ffffff;
  --ink:#1b1a1a;
  --accent:#acd136;
  --headline:#e6f23e;
  --photo-sky:#a7a4b8;
  --photo-field:#b39a7d;
}
*{box-sizing:border-box;margin:0;padding:0}
html,body{width:1194px;height:1200px;overflow:hidden;background:var(--gap)}
body{position:relative;font-family:"Advent Pro",sans-serif;color:var(--ink)}
.page{position:absolute;top:0;height:1200px;background:var(--panel);overflow:hidden}
.page--front{left:0;width:566px}
.page--back{left:628px;width:566px}
.hero-photo{position:absolute;left:0;top:0;width:566px;height:340px;
  background:linear-gradient(180deg,var(--photo-sky) 0%,#9d9e8c 35%,var(--photo-field) 70%,var(--panel) 100%)}
.block{position:absolute;font-size:23.5px;line-height:27px;font-weight:500;letter-spacing:-0.2px}
.hl{color:var(--accent)}
.headline{left:24px;top:16px;font-size:32px;line-height:34px;font-weight:500}
.headline .q{color:var(--headline)}
.intro{left:24px;top:160px}
.bullets{list-style:none}
.bullets li{position:absolute;padding-left:24px}
.bullets li::before{content:"";position:absolute;left:3px;top:10px;width:10px;height:10px;border:1.5px solid var(--ink);border-radius:50%}
.front-list li{left:24px;width:536px}
.back-list li{left:32px;width:534px;font-size:25px;line-height:29.5px;padding-left:23px;letter-spacing:-0.3px}
.back-list li::before{left:0;top:11px}
.nowrap{white-space:nowrap}
.photo{position:absolute;background:linear-gradient(135deg,#8b7a68,#d8c6ad 55%,#5a5048)}
.photo--two{background:linear-gradient(135deg,#cfd2c8,#e7d2b6 50%,#8a8c8e)}
.portrait{position:absolute;left:86px;top:764px;width:233px;height:154px;background:linear-gradient(90deg,#cfcfd1,#f2f2f2 50%,#c9c9cb)}
.brand{position:absolute;left:70px;top:680px;font-family:"Raleway",sans-serif;font-weight:300;color:var(--accent);white-space:nowrap}
.brand-name{font-size:29px;letter-spacing:4px;line-height:36px}
.brand-role{font-size:18px;letter-spacing:3.2px;line-height:22px}
.contact{left:70px;top:942px;font-size:22px;line-height:29.5px}
</style>
</head>
<body>
<section class="page page--front">
  <div class="hero-photo" role="img" aria-label="Gelber Kleinwagen mit Koffern auf dem Dach in einem Sommerfeld"></div>
  <h1 class="block headline">Wollen Sie<br><span class="q">Fahrangst überwinden?<br>Panikattacken beim Autofahren loswerden?<br>Oder einfach sicher Autofahren?</span></h1>
  <p class="block intro">Dann sind Sie hier richtig!<br>Kommt Ihnen eine dieser Situationen bekannt vor?</p>
  <ul class="bullets front-list">
    <li class="block" style="top:243px">Angst oder Panikattacken begleiten Sie beim Autofahren. Vielleicht vermeiden Sie deshalb das Autofahren komplett. - Sie möchten <span class="hl">angstfrei und/oder ohne Panikattacken</span> fahren.</li>
    <li class="block" style="top:379px">Sie trauen sich das Autofahren nicht (mehr) zu. - Sie wünschen sich, <span class="hl">sicher, entspannt und stressfrei Auto zu fahren.</span></li>
    <li class="block" style="top:488px">Autofahren erleben Sie unter hoher Anspannung und Stress. - Sie wünschen sich, Autofahren <span class="hl">sicher und entspannt</span> zu erleben.</li>
    <li class="block" style="top:597px">Bestimmte Situationen (z.B. Autobahn, Baustellen, Stadtvekehr...) bereiten Ihnen großen Stress. - Sie möchten diese Situationen <span class="hl">souveräner</span> meistern.</li>
  </ul>
  <p class="block" style="left:24px;top:706px">Das muss nicht so bleiben!</p>
  <p class="block" style="left:24px;top:760px">3 Schritte zur Lösung:</p>
  <p class="block" style="left:24px;top:814px">1. Erstgespräch vereinbaren</p>
  <p class="block" style="left:24px;top:869px">2. Analyse Ihrer individuellen Situation und Zielsetzung</p>
  <p class="block" style="left:24px;top:923px;width:530px">3. Individuelles Coaching und Training<br>&nbsp;(ggf. Fahrangst-Therapie - als psychotherapeutische Heilpraktikerin bin&nbsp; ich auf Angst- und Panikstörungen spezialisiert)</p>
  <div class="photo" style="left:56px;top:1043px;width:209px;height:139px" role="img" aria-label="Zufriedene Fahrerin im Cabrio"></div>
  <div class="photo photo--two" style="left:294px;top:1043px;width:208px;height:139px" role="img" aria-label="Lächelnde junge Fahrerin am Autofenster mit Daumen hoch"></div>
</section>

<section class="page page--back">
  <ul class="bullets back-list">
    <li class="block" style="top:107px">über 10 Jahre Erfahrung als <span class="hl">Trainerin und Coach</span> im Bereich <span class="hl">Fahrsicherheit.</span></li>
    <li class="block" style="top:196px">Als <span class="hl">psychotherapeutische Heilpraktikerin</span> bin ich <span class="hl">auf Angststörungen und Panikattacken spezialisiert.</span></li>
    <li class="block" style="top:284px"><span class="hl">100 % auf Sie zugeschnitten:</span> ich hole Sie genau dort ab, wo Sie jetzt stehen und unterstütze Sie in <span class="hl">Ihrem Prozess individuell und zielführend.</span></li>
    <li class="block" style="top:402px">Wenn es Ihnen nicht möglich ist, in meine Praxis nach Talheim Nord zu kommen: Mit der <span class="hl">mobilen Praxis komme ich auch zu Ihnen.</span></li>
    <li class="block nowrap" style="top:520px"><span class="hl">Termine</span> sind auch a<span class="hl">bends und am Wochenende möglich.</span></li>
  </ul>
  <div class="brand">
    <div class="brand-name">Carla Wendtner</div>
    <div class="brand-role">Fahrsicher-Coaching</div>
  </div>
  <div class="portrait" role="img" aria-label="Porträt der Trainerin in weißer Bluse"></div>
  <p class="block contact">Weitere Informationen finden Sie auf:<br>www.fahrsicher-coaching.de<br>Oder rufen Sie mich einfach an:<br>Tel. 0151 23 45 67 89</p>
</section>
</body>
</html>
```